【 概要 】 当社では、M&A業界に転職を考える求職者向けの転職支援サービスの立ち上げを行っています。 サイト名は「M&A WORK HARBOR」と言い、当社が運営する法律専門職向け転職サイト「LEGAL WORK HARBOR」の姉妹サイトです。 https://legal-work-harbor-example.com/ そのサービス(M&A WORK HARBOR)のLPのファーストビュー部分のデザインを依頼したいと思います。 【コンペ内容】 ワイヤーフレーム(PC)のファーストビュー付近に赤でラインを引いています。 そこまでのデザインでコンペをさせていただきます。 【 依頼内容 】 ・依頼工程:デザインのみ ・作業ボリューム:PC・スマホ1P(コンペはファーストビューのみ) 【 提供素材 】 ・ワイヤー、ラフ案:PCのみあり (添付PDF参照) ・画像:あり (添付画像参照、我々のイメージに近い写真を選定していますが、より良いイメージがあればご提案いただいても構いません。) 【 デザインイメージ 】 ・ターゲットペルソナ:29歳金融業界(大手メガバンク、証券会社)の男性。 ・雰囲気:シンプルでスタイリッシュ、モダンかつ高級感のあるデザイン。 ・参考サイト:https://kvemu-example.co.jp/lp/ 【ロゴについて】 添付します 【その他デザイン参考ページ】 https://legal-work-harbor-example.com/lawyer/lp/steps/ ↑当社の別サービスのデザインです 【 納期 】 2024年2月14日 ※コンペ以外のデザイン部分に関しては、コンペ終了後1〜2週間程度を想定しています。 【 報酬 】 12万円 【 追加依頼 】 HTMLコーディングの追加発注も検討しています。 総額20万くらいでHTMLまで完成させたいと考えていますので、追加8万ほどで発注できればと考えております。 ご検討よろしくお願いします。 HTMLに自信がなければ、その部分のみ他の方に発注も可能です。 ご質問がありましたら、気軽にお問い合わせください。 応募をお待ちしております! |
採用の理由
・修正案のイメージが非常に良かったこと
・コーディングまでの依頼が一気通貫でできること
・ポートフォリオからデザイン力が保証できることが理解できたこと
から採用させていただきます。
引き続きよろしくお願いします!
応募者全員へのお礼・コメント
みなさまからの多くのご提案大変ありがとうございました。
今回採用させていただいた理由として
・こちらの意図をよく理解してデザインに反映してくれたこと(修正案もいただきましたが、さらにクオリティが上がっていました)
ことなどを理由に採用させていただきました。
またご機会がありましたら、何卒よろしくお願いいたします。

```html
<!DOCTYPE html>
<html lang="ja">
<head>
<meta charset="utf-8">
<title>M&amp;A WORK HARBOR</title>
<link rel="stylesheet" href="https://fonts.googleapis.com/css2?family=Noto+Serif+JP:wght@500;700&family=Noto+Sans+JP:wght@400;500;700&family=Montserrat:wght@600;700&display=swap">
<style>
:root{
  --navy:#14223b;
  --navy-deep:#0c1628;
  --navy-card:#1b2a45;
  --gold:#c9ab6a;
  --white:#ffffff;
  --ink:#1a1f2b;
  --line:#9aa3b2;
  --muted:#5b6475;
}
*{box-sizing:border-box;margin:0;padding:0}
html,body{width:1200px;height:1149px;overflow:hidden;background:var(--white)}
body{font-family:"Noto Sans JP",sans-serif;color:var(--ink);position:relative}
.site-header{height:97px;text-align:center;padding-top:22px}
.brand{font-family:"Montserrat",sans-serif;font-weight:700;font-size:30px;letter-spacing:2px;color:var(--navy)}
.tagline{font-size:14px;letter-spacing:3px;margin-top:6px;color:var(--ink)}
.hero{position:absolute;top:97px;left:0;width:1200px;height:643px;background:var(--navy-deep);overflow:hidden}
.hero-photo{position:absolute;inset:0;background:
  radial-gradient(ellipse 420px 520px at 560px 300px,#6b6a70 0%,#3a4254 45%,rgba(12,22,40,0) 80%),
  linear-gradient(90deg,#0c1628 0%,#1d2b45 40%,#2a3650 60%,#0c1628 100%)}
.hero-copy{position:absolute;left:46px;top:140px}
.headline{font-family:"Noto Serif JP",serif;font-weight:700;font-size:62px;line-height:86px;color:var(--white);letter-spacing:2px}
.headline .accent{color:var(--gold)}
.lead{margin-top:34px;font-family:"Noto Serif JP",serif;font-size:16px;line-height:30px;color:var(--white);letter-spacing:1px}
.badge{position:absolute;z-index:3;left:746px;top:14px;width:84px;height:84px;background:var(--gold);border-radius:50%;color:var(--white);text-align:center;font-weight:700;display:flex;flex-direction:column;align-items:center;justify-content:center;line-height:1.1}
.badge .badge-label{font-size:14px}
.badge .badge-time{font-family:"Noto Serif JP",serif;font-size:16px;white-space:nowrap}
.badge .badge-time b{font-family:"Montserrat",sans-serif;font-size:24px}
.form-card{position:absolute;z-index:2;left:790px;top:52px;width:346px;height:556px;background:var(--white);border-radius:8px;overflow:hidden}
.form-title{background:var(--navy-card);color:var(--white);font-family:"Noto Serif JP",serif;font-weight:700;font-size:17px;height:56px;line-height:56px;padding-left:54px;white-space:nowrap}
.steps{display:flex;gap:6px;padding:16px 20px 0}
.steps span{flex:1;border:1px solid var(--line);font-size:10px;text-align:center;padding:3px 0;color:var(--muted)}
.steps span.current{background:var(--navy);color:var(--white);border-color:var(--navy)}
.field{padding:0 20px;margin-top:22px}
.field label{display:block;font-size:13px;font-weight:700;margin-bottom:6px}
.field label small{font-size:9px;color:var(--muted);font-weight:400;margin-left:4px}
.field .input{height:46px;border:1px solid var(--line);border-radius:4px}
.submit{position:absolute;left:70px;bottom:22px;width:206px;height:46px;background:var(--navy);color:var(--white);border-radius:10px;text-align:center;line-height:46px;font-weight:700;font-size:15px}
.reasons-title{position:absolute;top:776px;width:100%;text-align:center;font-size:22px;font-weight:700;color:var(--ink)}
.reasons-title .brand-inline{font-family:"Montserrat",sans-serif;font-size:34px;letter-spacing:3px;color:var(--navy);margin-right:10px}
.reasons{position:absolute;top:863px;left:46px;display:flex;gap:38px}
.reason{width:344px;height:235px;background:linear-gradient(160deg,#2a3954,#14223b);color:var(--white);padding:26px 24px}
.reason h3{font-family:"Noto Serif JP",serif;font-weight:700;font-size:27px;line-height:40px;text-align:center;padding-bottom:18px;white-space:nowrap}
.reason p{font-size:12.5px;line-height:22px}
</style>
</head>
<body>
<header class="site-header">
  <div class="brand">M&amp;A WORK HARBOR</div>
  <p class="tagline">M&amp;A業界の転職に、有能なパートナーを。</p>
</header>

<section class="hero">
  <div class="hero-photo" role="img" aria-label="スーツ姿のビジネスパーソンと夜のビル街の写真"></div>
  <div class="hero-copy">
    <h1 class="headline"><span class="accent">M&amp;A業界</span>への<br><span class="accent">転職</span>には、<br>パートナーが<br>必要だ。</h1>
    <p class="lead">M&amp;A WORK HARBORは、M&amp;A業界を経験した専門の<br>キャリアアドバイザーによる転職支援サービスです。</p>
  </div>
  <div class="badge"><span class="badge-label">登録</span><span class="badge-time"><b>60</b>秒</span></div>
  <form class="form-card">
    <div class="form-title">M&amp;A専門アドバイザーに相談する</div>
    <div class="steps"><span class="current">プロフィール</span><span>希望条件</span><span>登録完了</span></div>
    <div class="field"><label>お名前<small>※必須</small></label><div class="input"></div></div>
    <div class="field"><label>メールアドレス<small>※必須</small></label><div class="input"></div></div>
    <div class="field"><label>電話番号<small>※必須</small></label><div class="input"></div></div>
    <div class="field"><label>生年月日<small>※必須</small></label><div class="input"></div></div>
    <div class="submit">次へ</div>
  </form>
</section>

<h2 class="reasons-title"><span class="brand-inline">M&amp;A WORK HARBOR</span>が選ばれる理由</h2>
<div class="reasons">
  <article class="reason">
    <h3>エージェント自身が<br>M&amp;Aのプロ</h3>
    <p>エージェント自身がM&amp;A事業を経験しているため、紹介企業の特性を理解し、最適な企業の提案が可能。</p>
  </article>
  <article class="reason">
    <h3>まずは情報収集に最適</h3>
    <p>気軽にセッティングできるオンラインカウンセリングで、業界知識を深める。</p>
  </article>
  <article class="reason">
    <h3>大手M&amp;A企業と<br>繋がるパイプ</h3>
    <p>紹介先のほとんどは経営者クラスとの独自のパイプを構築済み。<br>選考を戦略的に進めます。</p>
  </article>
</div>
</body>
</html>
```